Lumo Voyages
business cards & letterhead
Lumo Voyages -
Creative Brief
Bright & Fun-filled
Corinne Maddox
58214 Birchwood Ln Rockville, MD 20817
lumovoyages@quellnet.example

```html
<!DOCTYPE html>
<html lang="en">
<head>
<meta charset="utf-8">
<title>Lumo Voyages – Business Card</title>
<link href="https://fonts.googleapis.com/css2?family=Nunito:wght@700;800&family=Open+Sans:wght@400;600&display=swap" rel="stylesheet">
<style>
  :root {
    --bg: #eceef1;
    --card: #ffffff;
    --blue: #1f7cc4;
    --blue-light: #3b9ade;
    --green: #a6c832;
    --ink: #4a4f55;
    --muted: #8a9097;
    --rule: #c9cdd2;
  }
  html, body {
    margin: 0;
    width: 1200px;
    height: 646px;
    overflow: hidden;
    background: var(--bg);
  }
  .stage {
    position: relative;
    width: 1200px;
    height: 646px;
  }
  .card {
    position: absolute;
    top: 173px;
    width: 540px;
    height: 300px;
    background: var(--card);
    box-shadow: 0 6px 18px rgba(0,0,0,0.12);
    overflow: hidden;
  }
  .card--front { left: 40px; }
  .card--back { left: 620px; }

  .brand {
    position: absolute;
    display: flex;
    align-items: center;
    gap: 12px;
  }
  .card--front .brand { left: 50%; top: 50%; transform: translate(-50%, -50%); }
  .card--back .brand { left: 30px; top: 200px; gap: 10px; }
  .brand__dot {
    width: 46px;
    height: 46px;
    border-radius: 50%;
    background: var(--blue);
    flex: none;
  }
  .card--back .brand__dot { width: 40px; height: 40px; }
  .brand__text { display: flex; flex-direction: column; }
  .brand__name {
    font-family: "Nunito", sans-serif;
    font-weight: 800;
    font-size: 30px;
    line-height: 1;
    color: var(--blue);
    white-space: nowrap;
  }
  .card--back .brand__name { font-size: 26px; }
  .brand__tagline {
    font-family: "Open Sans", sans-serif;
    font-size: 9px;
    color: var(--muted);
    margin-top: 4px;
    letter-spacing: 0.3px;
    white-space: nowrap;
  }

  .swoosh {
    position: absolute;
    left: 0;
    top: 0;
    width: 540px;
    height: 300px;
  }
  .holder-name {
    position: absolute;
    right: 28px;
    top: 30px;
    font-family: "Nunito", sans-serif;
    font-weight: 700;
    font-size: 19px;
    color: #ffffff;
    white-space: nowrap;
  }
  .contact {
    position: absolute;
    left: 318px;
    right: 14px;
    top: 160px;
    height: 110px;
    padding-left: 14px;
    border-left: 1px solid var(--rule);
    font-family: "Open Sans", sans-serif;
    font-size: 11px;
    color: var(--ink);
    line-height: 1.5;
    white-space: nowrap;
  }
  .contact__address { margin: 0 0 10px; }
  .contact__line {
    display: flex;
    align-items: center;
    gap: 6px;
    margin: 0 0 4px;
  }
  .contact__icon { width: 11px; height: 11px; flex: none; }
</style>
</head>
<body>
<main class="stage">

  <section class="card card--front" aria-label="Card front">
    <div class="brand">
      <span class="brand__dot"></span>
      <div class="brand__text">
        <span class="brand__name">Lumo Voyages</span>
        <span class="brand__tagline">your trip, your way</span>
      </div>
    </div>
  </section>

  <section class="card card--back" aria-label="Card back">
    <svg class="swoosh" viewBox="0 0 540 300" aria-hidden="true">
      <defs>
        <linearGradient id="bandBlue" x1="0" y1="0" x2="1" y2="0">
          <stop offset="0" stop-color="#1f7cc4"/>
          <stop offset="1" stop-color="#3b9ade"/>
        </linearGradient>
      </defs>
      <path d="M0 0 H540 V78 Q430 84 340 150 Q220 70 0 108 Z" fill="url(#bandBlue)"/>
      <path d="M0 116 Q220 78 340 160 Q430 96 540 88 V98 Q430 106 340 174 Q220 92 0 126 Z" fill="#a6c832"/>
    </svg>

    <span class="holder-name">Corinne Maddox</span>

    <div class="brand">
      <span class="brand__dot"></span>
      <div class="brand__text">
        <span class="brand__name">Lumo Voyages</span>
        <span class="brand__tagline">your trip, your way</span>
      </div>
    </div>

    <div class="contact">
      <p class="contact__address">58214 Birchwood Ln<br>Rockville, MD 20817</p>
      <p class="contact__line">
        <svg class="contact__icon" viewBox="0 0 12 12" aria-hidden="true"><path d="M3 1 L5 3.5 L4 5 Q5 7 7 8 L8.5 7 L11 9 L9.5 11 Q4 10.5 1 3 Z" fill="#1f7cc4"/></svg>
        (301) 555-0148
      </p>
      <p class="contact__line">
        <svg class="contact__icon" viewBox="0 0 12 12" aria-hidden="true"><rect x="1" y="2.5" width="10" height="7" rx="1" fill="none" stroke="#1f7cc4" stroke-width="1.2"/><path d="M1.5 3 L6 6.5 L10.5 3" fill="none" stroke="#1f7cc4" stroke-width="1.2"/></svg>
        lumovoyages@quellnet.example
      </p>
    </div>
  </section>

</main>
</body>
</html>
```